Offer banner redesign / Simplifying existing banner

We have a banner there customer can click on to get an offer. We want to simplify this banner and to get it to at minimum. We are not clear about how it shoulderstand look like, but the actual banner you can see here (It's at the top of the page): https://kaminwerk-vorhof.de/rauchrohr-stahl/ We want to get rid of the icons and to reduce the size of the baner. The baner shoulderstand contain the Following text: Affordable chimney using installation service button text: Request free quote

Target Market(s)

Customers from age of 40yrs.

Requirements
Must have
• Clear and good visible button
Nice to have
• It Should be simple and striking.

```html
<!DOCTYPE html>
<html lang="de">
<head>
<meta charset="utf-8">
<title>Angebotsbanner – Preiswerter Schornstein</title>
<link rel="stylesheet" href="https://fonts.googleapis.com/css2?family=Exo+2:wght@400;500;600&display=swap">
<style>
  :root {
    --stage-blue: #0a7fc0;
    --card-bg: #f4f4f4;
    --ink: #1c1c1c;
    --accent: #f9b233;
    --button-border: #9a8a6a;
  }
  * { margin: 0; padding: 0; box-sizing: border-box; }
  html, body { width: 1200px; height: 1000px; overflow: hidden; }
  body {
    background: var(--stage-blue);
    font-family: "Exo 2", sans-serif;
    color: var(--ink);
    position: relative;
  }
  .banner { position: absolute; background: var(--card-bg); }

  .banner--square {
    left: 335px; top: 156px; width: 531px; height: 443px;
    display: flex; flex-direction: column; align-items: center;
    padding-top: 58px;
  }
  .banner--square .flame-icon { width: 50px; height: 50px; }
  .banner--square .benefit {
    font-size: 30px; font-weight: 500; line-height: 1;
    margin: 8px 0 10px;
  }
  .banner--square .cta {
    margin-top: 36px; width: 384px; height: 76px; font-size: 21px;
  }

  .banner--strip {
    left: 174px; top: 736px; width: 851px; height: 106px;
  }
  .benefit-row {
    position: absolute; left: 16px;
    display: flex; align-items: center; gap: 8px;
    font-size: 23px; font-weight: 500;
  }
  .benefit-row .flame-icon { width: 32px; height: 32px; }
  .benefit-row--first { top: 11px; }
  .benefit-row--second { top: 62px; }
  .banner--strip .cta {
    position: absolute; left: 431px; top: 31px;
    width: 392px; height: 44px; font-size: 22px;
  }

  .cta {
    display: flex; align-items: center; justify-content: center;
    background: var(--accent);
    border: 1px solid var(--button-border);
    border-radius: 999px;
    font-weight: 600; color: var(--ink);
    text-decoration: none;
  }
</style>
</head>
<body>
  <section class="banner banner--square">
    <svg class="flame-icon" viewBox="0 0 50 50" aria-hidden="true">
      <circle cx="25" cy="25" r="22" fill="none" stroke="var(--accent)" stroke-width="3"/>
      <path d="M25 9c2 6 10 11 10 21a10 10 0 0 1-20 0c0-5 3-8 5-10 0 4 2 6 4 6-3-6 0-12 1-17z" fill="var(--accent)"/>
    </svg>
    <p class="benefit">Preiswerter Schornstein</p>
    <svg class="flame-icon" viewBox="0 0 50 50" aria-hidden="true">
      <circle cx="25" cy="25" r="22" fill="none" stroke="var(--accent)" stroke-width="3"/>
      <path d="M25 9c2 6 10 11 10 21a10 10 0 0 1-20 0c0-5 3-8 5-10 0 4 2 6 4 6-3-6 0-12 1-17z" fill="var(--accent)"/>
    </svg>
    <p class="benefit">wahlweise mit Montageservice</p>
    <a class="cta" href="#angebot">kostenloses Angebot anfordern</a>
  </section>

  <section class="banner banner--strip">
    <div class="benefit-row benefit-row--first">
      <svg class="flame-icon" viewBox="0 0 50 50" aria-hidden="true">
        <circle cx="25" cy="25" r="22" fill="none" stroke="var(--accent)" stroke-width="3"/>
        <path d="M25 9c2 6 10 11 10 21a10 10 0 0 1-20 0c0-5 3-8 5-10 0 4 2 6 4 6-3-6 0-12 1-17z" fill="var(--accent)"/>
      </svg>
      <span>Preiswerter Schornstein</span>
    </div>
    <div class="benefit-row benefit-row--second">
      <svg class="flame-icon" viewBox="0 0 50 50" aria-hidden="true">
        <circle cx="25" cy="25" r="22" fill="none" stroke="var(--accent)" stroke-width="3"/>
        <path d="M25 9c2 6 10 11 10 21a10 10 0 0 1-20 0c0-5 3-8 5-10 0 4 2 6 4 6-3-6 0-12 1-17z" fill="var(--accent)"/>
      </svg>
      <span>wahlweise mit Montageservice</span>
    </div>
    <a class="cta" href="#angebot">kostenloses Angebot anfordern</a>
  </section>
</body>
</html>
```